Business card/stationary for non profit organization
Business card and Stationary for non profit organization
Business card/stationary for non profit organization - Children
Creative Brief
Bright & Fun-filled
Mr. Fenwick
Founder
517 Bellmore Lane Suite 309 Harlow Ridge, New York 10599
fenwick@mrfenwickcommons.org
www.mrfenwickcommons.org
Please have the logo on the back of the business card and room for a tagline.
Concepts
Business Cards for kids golf

```html
<!DOCTYPE html>
<html lang="en">
<head>
<meta charset="utf-8">
<title>Mr. Fenwick Commons — Business Card</title>
<link rel="stylesheet" href="https://fonts.googleapis.com/css2?family=Open+Sans:wght@400;600;700&display=swap">
<style>
  :root {
    --backdrop: #d9d7d3;
    --card-black: #1f1d1e;
    --gold: #d4bd52;
    --gold-light: #ede08e;
    --gold-deep: #a88f2a;
    --text-light: #e6e4df;
    --text-muted: #b9b6ae;
  }
  * { margin: 0; padding: 0; box-sizing: border-box; }
  html, body {
    width: 1200px; height: 839px; overflow: hidden;
    background: var(--backdrop);
    font-family: "Open Sans", Arial, sans-serif;
  }
  .stage { position: relative; width: 1200px; height: 839px; }
  .card {
    position: absolute;
    width: 550px; height: 314px;
    background: var(--card-black);
    border-radius: 4px;
    box-shadow: 0 6px 18px rgba(0,0,0,.25);
    overflow: hidden;
  }
  .card-back { left: 600px; top: 70px; }
  .card-front { left: 50px; top: 430px; }

  /* logo stand-in */
  .brand-mark {
    display: flex; align-items: center; gap: 12px;
    color: var(--gold);
    font-weight: 700;
    text-transform: uppercase;
    letter-spacing: .04em;
  }
  .brand-dot {
    border-radius: 50%;
    background: var(--gold);
    flex: none;
  }
  .card-back .brand-mark {
    position: absolute; left: 50%; top: 92px;
    transform: translateX(-50%);
    font-size: 24px; white-space: nowrap;
  }
  .card-back .brand-dot { width: 46px; height: 46px; }
  .back-url {
    position: absolute; left: 0; right: 0; top: 228px;
    text-align: center;
    color: var(--text-light);
    font-size: 14px; letter-spacing: .12em;
  }

  .card-front .brand-mark {
    position: absolute; left: 28px; top: 34px;
    font-size: 16px; line-height: 1.15;
  }
  .card-front .brand-dot { width: 34px; height: 34px; }
  .swoosh { position: absolute; left: 0; top: 0; width: 550px; height: 314px; }

  .contact {
    position: absolute; left: 286px; top: 34px;
    color: var(--text-light);
    font-size: 12px; line-height: 1.4;
  }
  .contact-name { font-weight: 700; font-size: 13px; color: var(--gold-light); }
  .contact-role { color: var(--text-muted); margin-bottom: 22px; }
  .contact-address { margin-bottom: 22px; }
</style>
</head>
<body>
<main class="stage">

  <section class="card card-back" aria-label="Card back">
    <div class="brand-mark"><span class="brand-dot"></span>Mr. Fenwick Commons</div>
    <p class="back-url">www.mrfenwickcommons.org</p>
  </section>

  <section class="card card-front" aria-label="Card front">
    <svg class="swoosh" viewBox="0 0 550 314" aria-hidden="true">
      <path d="M0 150 C 120 190, 260 250, 420 314 L 0 314 Z" fill="var(--gold-deep)"/>
      <path d="M0 172 C 130 215, 270 262, 400 314 L 0 314 Z" fill="var(--card-black)"/>
      <path d="M0 184 C 140 228, 280 272, 390 314 L 0 314 Z" fill="var(--gold-light)"/>
      <path d="M0 222 C 150 250, 290 286, 360 314 L 0 314 Z" fill="var(--gold)"/>
      <path d="M0 258 C 120 272, 230 294, 290 314 L 0 314 Z" fill="var(--gold-deep)"/>
    </svg>

    <div class="brand-mark"><span class="brand-dot"></span>Mr. Fenwick<br>Commons</div>

    <div class="contact">
      <p class="contact-name">Mr. Fenwick</p>
      <p class="contact-role">Founder</p>
      <p class="contact-address">517 Bellmore Lane Suite 309<br>Harlow Ridge, New York 10599</p>
      <p>Tel: 555-210-0142</p>
      <p>Fax: 555-210-0143</p>
      <p>Email: fenwick@mrfenwickcommons.org</p>
      <p>www.mrfenwickcommons.org</p>
    </div>
  </section>

</main>
</body>
</html>
```